I need a professional modern flyer offering our crane services with our phone number and website. The flyer should focus on the blue crane and the red crane (JointArms) but include a small picture of the other cranes as well to show variety. This flyer will be mailed and emailed to a variety of roofing companies, HVAC, pool and mechanical contractors as well as precast concrete companies to attempt to earn their business. 8.5x11 single sided

HoistReadyRigging.example
555 814-2967 should be number on flyer

```html
<!DOCTYPE html>
<html lang="en">
<head>
<meta charset="utf-8">
<title>Hoist Ready Rigging – Crane Service Flyer</title>
<link rel="stylesheet" href="https://fonts.googleapis.com/css2?family=Exo+2:ital,wght@0,400;0,600;0,700;0,800;1,400&family=Saira+Condensed:wght@700;800&display=swap">
<style>
  :root {
    --red: #d3242c;
    --deep-red: #7d1015;
    --ink: #111111;
    --charcoal: #2a2b2e;
    --paper: #ffffff;
    --steel: #8d9198;
    --stage: #101010;
  }
  * { box-sizing: border-box; margin: 0; padding: 0; }
  html, body { width: 1200px; height: 1200px; overflow: hidden; background: var(--stage); }
  body { font-family: "Exo 2", sans-serif; color: var(--ink); }

  .flyer {
    position: absolute; left: 175px; top: 50px;
    width: 850px; height: 1100px;
    background: var(--paper); overflow: hidden;
  }
  .hero-photo {
    position: absolute; left: 0; top: 0; width: 850px; height: 470px;
    background: linear-gradient(180deg, #c9d2dc 0%, #d6dbe1 45%, #b9bcc1 72%, #f2f3f5 100%);
  }
  .hero-trucks {
    position: absolute; left: 40px; top: 270px; width: 800px; height: 180px;
    background: linear-gradient(90deg, #cfd2d6 0%, #e7e8ea 30%, #c4c9d3 55%, #2e4fa0 80%, #3a5bb0 100%);
    border-radius: 30px 30px 10px 10px; opacity: .85;
  }
  .red-blob, .black-blob { position: absolute; top: 0; }
  .red-blob { left: 0; }
  .black-blob { right: 0; }

  .brand {
    position: absolute; left: 42px; top: 96px; width: 220px;
    display: flex; align-items: center; gap: 8px;
    color: var(--paper); font-weight: 800; font-size: 19px; letter-spacing: .3px;
  }
  .brand-dot { width: 12px; height: 12px; background: var(--paper); flex: none; }

  .headline {
    position: absolute; left: 255px; top: 62px; width: 380px;
    font-family: "Saira Condensed", sans-serif; font-weight: 800;
    font-size: 42px; line-height: 44px; text-align: center;
  }
  .lede {
    position: absolute; left: 270px; top: 162px; width: 330px;
    font-size: 12.5px; line-height: 15px; text-align: center; color: var(--charcoal);
  }

  .services {
    position: absolute; left: 40px; top: 480px; width: 770px; height: 95px;
    display: flex; justify-content: space-between;
  }
  .service {
    flex: 1; display: flex; flex-direction: column; align-items: center; gap: 8px;
    border-right: 1.5px solid var(--charcoal);
  }
  .service:last-child { border-right: none; }
  .service svg { width: 54px; height: 46px; }
  .service-name { font-weight: 700; font-size: 14px; line-height: 16px; text-align: center; }

  .fleet {
    position: absolute; left: 38px; top: 637px; width: 782px;
    display: grid; grid-template-columns: repeat(4, 180px); column-gap: 20px; row-gap: 31px;
  }
  .fleet-card {
    position: relative; width: 180px; height: 131px;
    border: 1px solid var(--charcoal); background: #f4f5f6; overflow: hidden;
  }
  .fleet-card .card-shape { position: absolute; inset: 0; }
  .fleet-photo {
    position: absolute; left: 42px; top: 6px; width: 130px; height: 62px;
    border-radius: 8px; background: linear-gradient(135deg, #f2c21a 0%, #e0a412 55%, #3d3d3d 100%);
  }
  .fleet-photo.white { background: linear-gradient(135deg, #f1f1f1 0%, #c8ccd1 60%, #3a3a3a 100%); }
  .fleet-photo.red { background: linear-gradient(135deg, #e23a3a 0%, #b51f25 60%, #2d2d2d 100%); }
  .fleet-label {
    position: absolute; left: 6px; top: 94px; width: 116px; text-align: center;
    font-weight: 700; font-size: 9px; line-height: 11px; letter-spacing: .1px;
  }
  .fleet-model {
    display: block; font-weight: 400; font-style: italic; font-size: 8.5px; line-height: 10px;
    color: var(--steel);
  }

  .contact-band {
    position: absolute; left: 38px; top: 968px; width: 782px; height: 132px;
    background: linear-gradient(90deg, #1f2023 0%, #2f3034 35%, #25262a 65%, #1c1d20 100%);
  }
  .contact-pill {
    position: absolute; left: 204px; top: 51px; width: 372px; height: 70px;
    border-radius: 35px; background: var(--deep-red);
    display: flex; align-items: center; justify-content: center; gap: 14px; color: var(--paper);
  }
  .contact-pill svg { width: 38px; height: 38px; }
  .phone { font-weight: 800; font-size: 26px; line-height: 26px; }
  .web { font-size: 11px; }
</style>
</head>
<body>
<main class="flyer">
  <div class="hero-photo" role="img" aria-label="Crane trucks parked outside a commercial building"></div>
  <div class="hero-trucks" role="img" aria-label="Red knuckle-boom crane truck beside a blue knuckle-boom crane truck"></div>

  <svg class="red-blob" width="360" height="220" viewBox="0 0 360 220" aria-hidden="true">
    <path d="M0 0 H362 C350 80 300 140 220 170 C150 196 90 210 0 218 Z" fill="var(--red)"/>
  </svg>
  <svg class="black-blob" width="145" height="225" viewBox="0 0 145 225" aria-hidden="true">
    <path d="M145 0 H110 C90 0 80 10 70 30 L10 150 C-5 185 10 225 55 225 H145 Z" fill="var(--ink)"/>
  </svg>

  <div class="brand"><span class="brand-dot"></span>Hoist Ready Rigging</div>

  <h1 class="headline">CRANE SERVICE,<br>DONE AS PROMISED</h1>
  <p class="lede">Crane service partners that meet deadlines,<br>prioritize safety, and stay within budget<br>with end-to-end support.</p>

  <section class="services">
    <div class="service">
      <svg viewBox="0 0 54 46" fill="none" stroke="#111" stroke-width="1.6"><circle cx="16" cy="16" r="11"/><path d="M16 14v30M10 22l6 6 6-8"/><circle cx="38" cy="20" r="10"/><path d="M38 18v26M33 26l5 5 5-6M2 44h50"/></svg>
      <span class="service-name">TREE AND<br>LANDSCAPING</span>
    </div>
    <div class="service">
      <svg viewBox="0 0 54 46" fill="none" stroke="#111" stroke-width="1.6"><path d="M14 44V4h6v40M8 8h40M20 8l20 0v10M4 44h46"/><rect x="34" y="22" width="12" height="10"/><path d="M6 24h8M6 32h8M6 40h8"/></svg>
      <span class="service-name">STEEL<br>CONSTRUCTION</span>
    </div>
    <div class="service">
      <svg viewBox="0 0 54 46" fill="none" stroke="#111" stroke-width="1.6"><rect x="12" y="2" width="30" height="42"/><path d="M27 8v36M20 20v8M18 22l2-2 2 2M34 20v8M32 26l2 2 2-2"/></svg>
      <span class="service-name">HVAC<br>LIFTS</span>
    </div>
    <div class="service">
      <svg viewBox="0 0 54 46" fill="none" stroke="#111" stroke-width="1.6"><path d="M22 4h10l10 36H12Z M18 18h18M15 30h24M6 40h42"/><path d="M6 8l3 3M48 8l-3 3M4 20h4M46 20h4"/></svg>
      <span class="service-name">GENERAL<br>CONSTRUCTION</span>
    </div>
    <div class="service">
      <svg viewBox="0 0 54 46" fill="none" stroke="#111" stroke-width="1.6"><path d="M14 44V4h6v40M8 8h40M40 8v12M4 44h46"/><rect x="32" y="22" width="16" height="12"/><path d="M6 24h8M6 32h8M6 40h8"/></svg>
      <span class="service-name">CONTAINER<br>LIFTS</span>
    </div>
  </section>

  <section class="fleet">
    <article class="fleet-card">
      <svg class="card-shape" viewBox="0 0 180 131" preserveAspectRatio="none" aria-hidden="true"><path d="M60 0 H180 V131 H158 C140 131 134 96 112 90 H70 C50 90 40 74 40 56 V0 Z" fill="var(--deep-red)"/></svg>
      <div class="fleet-photo" role="img" aria-label="Yellow all-terrain crane"></div>
      <div class="fleet-label">ALL-TERRAIN CRANES<span class="fleet-model">RIDGELINE RT 40</span></div>
    </article>
    <article class="fleet-card">
      <svg class="card-shape" viewBox="0 0 180 131" preserveAspectRatio="none" aria-hidden="true"><path d="M60 0 H180 V131 H158 C140 131 134 96 112 90 H70 C50 90 40 74 40 56 V0 Z" fill="var(--deep-red)"/></svg>
      <div class="fleet-photo" role="img" aria-label="Orange all-terrain crane"></div>
      <div class="fleet-label">ALL-TERRAIN CRANES<span class="fleet-model">SUMMIT AT 80</span></div>
    </article>
    <article class="fleet-card">
      <svg class="card-shape" viewBox="0 0 180 131" preserveAspectRatio="none" aria-hidden="true"><path d="M60 0 H180 V131 H158 C140 131 134 96 112 90 H70 C50 90 40 74 40 56 V0 Z" fill="var(--deep-red)"/></svg>
      <div class="fleet-photo white" role="img" aria-label="White truck crane"></div>
      <div class="fleet-label">TRUCK CRANES<span class="fleet-model">CRESTWAY CT 42</span></div>
    </article>
    <article class="fleet-card">
      <svg class="card-shape" viewBox="0 0 180 131" preserveAspectRatio="none" aria-hidden="true"><path d="M60 0 H180 V131 H158 C140 131 134 96 112 90 H70 C50 90 40 74 40 56 V0 Z" fill="var(--deep-red)"/></svg>
      <div class="fleet-photo red" role="img" aria-label="Red rough-terrain forklift"></div>
      <div class="fleet-label">FORKLIFT<span class="fleet-model">TANDEM FL 6</span></div>
    </article>
    <article class="fleet-card">
      <svg class="card-shape" viewBox="0 0 180 131" preserveAspectRatio="none" aria-hidden="true"><path d="M60 0 H180 V131 H158 C140 131 134 96 112 90 H70 C50 90 40 74 40 56 V0 Z" fill="var(--deep-red)"/></svg>
      <div class="fleet-photo white" role="img" aria-label="White boom truck crane"></div>
      <div class="fleet-label">TRUCK CRANES<span class="fleet-model">BOOMCRAFT BT 30</span></div>
    </article>
    <article class="fleet-card">
      <svg class="card-shape" viewBox="0 0 180 131" preserveAspectRatio="none" aria-hidden="true"><path d="M60 0 H180 V131 H158 C140 131 134 96 112 90 H70 C50 90 40 74 40 56 V0 Z" fill="var(--deep-red)"/></svg>
      <div class="fleet-photo white" role="img" aria-label="White truck crane with extended boom"></div>
      <div class="fleet-label">TRUCK CRANES<span class="fleet-model">BOOMCRAFT BT 30</span></div>
    </article>
    <article class="fleet-card">
      <svg class="card-shape" viewBox="0 0 180 131" preserveAspectRatio="none" aria-hidden="true"><path d="M60 0 H180 V131 H158 C140 131 134 96 112 90 H70 C50 90 40 74 40 56 V0 Z" fill="var(--deep-red)"/></svg>
      <div class="fleet-photo" role="img" aria-label="Yellow all-terrain crane"></div>
      <div class="fleet-label">ALL-TERRAIN CRANES<span class="fleet-model">SUMMIT AT 80</span></div>
    </article>
    <article class="fleet-card">
      <svg class="card-shape" viewBox="0 0 180 131" preserveAspectRatio="none" aria-hidden="true"><path d="M60 0 H180 V131 H158 C140 131 134 96 112 90 H70 C50 90 40 74 40 56 V0 Z" fill="var(--deep-red)"/></svg>
      <div class="fleet-photo red" role="img" aria-label="Red truck crane"></div>
      <div class="fleet-label">TRUCK CRANES<span class="fleet-model">VANTOR VT 25</span></div>
    </article>
  </section>

  <footer class="contact-band" role="img" aria-label="Dusk view of crane trucks at job sites">
    <div class="contact-pill">
      <svg viewBox="0 0 38 38" fill="none" stroke="#fff" stroke-width="2.4" stroke-linecap="round" aria-hidden="true">
        <path d="M8 6c-3 2-4 6-2 11 3 7 8 12 15 15 5 2 9 1 11-2l-5-6-4 2c-3-1-6-4-7-7l2-4-5-6z" fill="#fff" stroke="none"/>
        <path d="M22 6a10 10 0 0 1 10 10M22 11a5 5 0 0 1 5 5"/>
      </svg>
      <div>
        <div class="phone">555 814-2967</div>
        <div class="web">HoistReadyRigging.example</div>
      </div>
    </div>
  </footer>
</main>
</body>
</html>
```